Webdesign für Data Engineers
Very creative approach and clear winner of competition. Looking forward to further cooperation. Matze
Zielgruppe
Wir machen big data Analytics (Auswertung großer und komplexer Unternehmens- und Web-Daten).
Unsere Kunden sind (große) Industrie- & Konsumgüterhersteller (z.B. Weisse Ware-Hersteller, aber auch online-Handelsunternehmen)
Aufgabenstellung
Uns gefallen Webseiten mit großen, ansprechenden Bildern, klarem Schriftbild und schneller Orientierung. z.B. vorniqa.com, quelmaritz.com
Die Farbgebung sollte sich an unserem Firmenlogo orientieren (blau, grau), das wir mit hochladen. Das Logo sollte natürlich auch präsent sein:-). Wichtig noch folgende Daten zum Logo:
Zur Schrift:
Hauptschrift: Titillium (Bold)
Subline + Fließtext: Antonio
Farben:
Hauptfarbe1: C= 100 M= 20 Y= 0 K=0
Hauptfarbe2: C= 40 M=20 Y=0 K=71
Farbe Subline: C=0 M=0 Y=0 K=50
Ausserdem wäre uns für die spätere Beauftragung noch folgendes wichtig:
- Umsetzung als "WordPress" CMS
- Englisch-Deutsch-Umschaltung
- Zusätzliche Mobilansicht

```html
<!DOCTYPE html>
<html lang="de">
<head>
<meta charset="utf-8">
<title>Quorvia Data – Mobile Startseite</title>
<link rel="stylesheet" href="https://fonts.googleapis.com/css2?family=Antonio:wght@400;600&family=Titillium+Web:wght@400;700&display=swap">
<style>
  :root {
    --brand-blue: #0099d8;
    --brand-dark: #2c3a4a;
    --subline-grey: #8a8a8a;
    --page-bg: #e9ecef;
    --panel-light: #f2f4f6;
    --white: #ffffff;
  }
  * { box-sizing: border-box; margin: 0; padding: 0; }
  html, body { width: 1200px; height: 801px; overflow: hidden; }
  body {
    background: var(--page-bg);
    display: flex;
    justify-content: center;
    font-family: "Antonio", "Arial Narrow", sans-serif;
  }
  .mobile-page {
    width: 460px;
    height: 801px;
    background: var(--white);
    display: flex;
    flex-direction: column;
    box-shadow: 0 0 24px rgba(0,0,0,0.08);
  }
  .site-header {
    height: 82px;
    display: flex;
    align-items: center;
    justify-content: space-between;
    padding: 0 26px;
    border-top: 6px solid var(--brand-blue);
  }
  .brand { display: flex; align-items: center; gap: 10px; }
  .brand-square { width: 30px; height: 30px; background: var(--brand-dark); }
  .brand-text { display: flex; flex-direction: column; line-height: 1; }
  .brand-name {
    font-family: "Titillium Web", sans-serif;
    font-weight: 700;
    font-size: 24px;
    color: var(--brand-dark);
  }
  .brand-tagline {
    font-size: 11px;
    letter-spacing: 1px;
    color: var(--subline-grey);
    margin-top: 4px;
    text-transform: uppercase;
  }
  .menu-toggle { width: 30px; height: 22px; display: flex; flex-direction: column; justify-content: space-between; }
  .menu-toggle span { height: 4px; background: var(--brand-blue); }
  .hero-image {
    height: 250px;
    background: linear-gradient(120deg, #f4f7fa 0%, #dfe8f0 40%, #3d5f8a 75%, #1f3554 100%);
  }
  .services-title {
    font-family: "Titillium Web", sans-serif;
    font-weight: 700;
    font-size: 30px;
    color: var(--brand-blue);
    padding: 14px 26px 10px;
  }
  .service {
    flex: 1;
    display: flex;
    align-items: center;
    gap: 20px;
    padding: 0 26px;
  }
  .service--blue { background: var(--brand-blue); color: var(--white); }
  .service--light { background: var(--panel-light); color: var(--brand-dark); }
  .service-icon { width: 56px; height: 56px; flex: none; }
  .service-name {
    font-family: "Titillium Web", sans-serif;
    font-weight: 700;
    font-size: 19px;
    line-height: 1.1;
  }
  .service--light .service-name { color: var(--brand-blue); }
  .service-text { font-size: 13px; line-height: 1.35; margin-top: 4px; }
  .service--light .service-text { color: var(--subline-grey); }
</style>
</head>
<body>
<main class="mobile-page">
  <header class="site-header">
    <div class="brand">
      <div class="brand-square"></div>
      <div class="brand-text">
        <span class="brand-name">Quorvia Data</span>
        <span class="brand-tagline">Big Data Analytics Beratung</span>
      </div>
    </div>
    <div class="menu-toggle" aria-label="Menü"><span></span><span></span><span></span></div>
  </header>

  <div class="hero-image" role="img" aria-label="Foto: Geschäftsleute besprechen Diagramme am Schreibtisch"></div>

  <h1 class="services-title">Unsere Services</h1>

  <section class="service service--blue">
    <svg class="service-icon" viewBox="0 0 56 56" fill="none" stroke="#fff" stroke-width="3">
      <rect x="8" y="8" width="40" height="28"/>
      <line x1="28" y1="36" x2="20" y2="50"/><line x1="28" y1="36" x2="36" y2="50"/>
      <polyline points="14,30 22,22 28,26 40,14"/>
    </svg>
    <div>
      <h2 class="service-name">Data Asset Valuation</h2>
      <p class="service-text">Wir bewerten Ihre Datenbestände und zeigen, welchen Wert Ihre Unternehmensdaten heute schon haben und wie Sie daraus konkrete Potenziale ableiten.</p>
    </div>
  </section>

  <section class="service service--light">
    <svg class="service-icon" viewBox="0 0 56 56" fill="none" stroke="#2c3a4a" stroke-width="4">
      <circle cx="23" cy="23" r="14"/>
      <line x1="33" y1="33" x2="48" y2="48" stroke-linecap="round"/>
    </svg>
    <div>
      <h2 class="service-name">Data Use Case Exploration</h2>
      <p class="service-text">Gemeinsam mit Ihnen finden wir passende Anwendungsfälle, prüfen verfügbare Quellen und priorisieren Ideen nach Nutzen, Aufwand und Machbarkeit im Unternehmen.</p>
    </div>
  </section>

  <section class="service service--blue">
    <svg class="service-icon" viewBox="0 0 56 56" fill="none" stroke="#fff" stroke-width="3">
      <path d="M14 40 a9 9 0 0 1 1-18 a12 12 0 0 1 23-3 a10 10 0 0 1 4 21 z"/>
      <line x1="22" y1="40" x2="22" y2="30"/><line x1="28" y1="40" x2="28" y2="26"/><line x1="34" y1="40" x2="34" y2="32"/>
    </svg>
    <div>
      <h2 class="service-name">Data Use Case Automation</h2>
      <p class="service-text">Wir automatisieren Ihre Analysen mit robusten Datenstrecken, damit Ergebnisse verlässlich, schnell und ohne manuellen Aufwand in Ihre Prozesse fließen.</p>
    </div>
  </section>

  <section class="service service--light">
    <svg class="service-icon" viewBox="0 0 56 56" fill="none" stroke="#2c3a4a">
      <circle cx="20" cy="32" r="11" stroke-width="7" stroke-dasharray="4 3"/>
      <circle cx="20" cy="32" r="5" stroke-width="3"/>
      <circle cx="39" cy="18" r="8" stroke-width="6" stroke-dasharray="3 3"/>
      <circle cx="39" cy="18" r="3" stroke-width="2.5"/>
    </svg>
    <div>
      <h2 class="service-name">Use Case Operation</h2>
      <p class="service-text">Im laufenden Betrieb überwachen und pflegen wir Ihre Lösungen, passen Modelle an neue Daten an und sichern dauerhaft stabile Ergebnisse.</p>
    </div>
  </section>
</main>
</body>
</html>
```